KEV.PRO- Darren Holcombe Fitness- needs a clever business card using the logo, name, info, contact

I need a business card designed for my Online Personal Training company called KEV.PRO, abbreviation for Darren Holcombe Fitness. My company focuses on coaching in personal health and personal growth to unleash your greatest potential. I would like to see designs that use my color scheme of a redish-orange (C:0,M:84,Y:100,K:0), grey, white, black, and my company font is OSWALD. The final design should communicate some aspects of design, health, motivation, growth, in some way. The logo is very important to the company and can be displayed in any of the colors previously mentioned. Must include the company name, my website: www.kev-pro.example , my email: dan@kev-pro.example

Target Market(s)

Personal health, fitness, general public, those who lack knowledge, awareness, and confidence in personal health

Industry/Entity Type

Personal Trainer

Font styles to use
Other font styles liked:
• OSWALD. (Bold, Regular, Light)

Colors
f37122
ffffff
9d9d9d
000000

Requirements
Must have
• Must include the logo, company name, my website: www.kev-pro.example , my email: dan@kev-pro.example
Nice to have
• Variations of the colors scheme of a redish-orange (C:0,M:84,Y:100,K:0), grey, white, black. Logo, card, or text can be in any of these colors.
• Possible quote like "Take control of your personal health to unleash your greatest potential" or "Unleashing your greatness first begins with fitness of the body and mind"

```html
<!DOCTYPE html>
<html lang="en">
<head>
<meta charset="utf-8">
<title>KEV.PRO Business Card</title>
<link rel="stylesheet" href="https://fonts.googleapis.com/css2?family=Oswald:wght@300;400;500;700&display=swap">
<style>
  :root {
    --orange: #f37122;
    --white: #ffffff;
    --grey: #9d9d9d;
    --black: #000000;
    --backdrop: #e2c6b7;
  }
  * { margin: 0; padding: 0; box-sizing: border-box; }
  html, body {
    width: 1200px; height: 800px; overflow: hidden;
    background: var(--backdrop);
    font-family: "Oswald", "Arial Narrow", sans-serif;
  }
  .canvas { position: relative; width: 1200px; height: 800px; }
  .card {
    position: absolute; top: 192px;
    width: 237px; height: 395px;
    background: var(--white); overflow: hidden;
  }
  .card--front { left: 313px; }
  .card--back  { left: 651px; }

  /* Front */
  .brand { position: absolute; top: 0; left: 0; right: 0; height: 232px; text-align: center; }
  .brand__dot {
    position: absolute; left: 50%; top: 44px;
    width: 96px; height: 96px; margin-left: -48px;
    border-radius: 50%; background: var(--orange);
  }
  .brand__name {
    position: absolute; left: 0; right: 0; top: 156px;
    font-weight: 700; font-size: 21px; line-height: 1; color: var(--black);
    letter-spacing: -0.2px;
  }
  .brand__tagline {
    position: absolute; left: 0; right: 0; top: 181px;
    font-weight: 400; font-size: 5.5px; line-height: 1; color: var(--black);
    text-transform: uppercase;
  }
  .contact {
    position: absolute; left: 0; right: 0; bottom: 0; height: 163px;
    background: var(--orange); color: var(--white);
    text-align: center; padding-top: 20px;
  }
  .contact__line { font-size: 12px; line-height: 21px; text-transform: uppercase; }
  .contact__label { font-weight: 300; margin-right: 4px; }
  .contact__value { font-weight: 500; }

  /* Back */
  .tab {
    position: absolute; left: 0; top: 78px;
    width: 19px; height: 8px; border-radius: 0 4px 4px 0;
    background: var(--grey);
  }
  .quote { position: absolute; left: 30px; top: 72px; color: var(--black); text-transform: uppercase; line-height: 1; }
  .quote__line { display: block; font-weight: 300; }
  .quote__line--lead  { font-size: 18px; }
  .quote__line--small { font-size: 12px; margin-top: 3px; }
  .quote__line--indent { margin-left: 39px; margin-top: 6px; }
  .quote__line--close { font-size: 19px; margin-left: 39px; margin-top: 2px; }
  .accent { color: var(--orange); font-weight: 400; }
  .signature-band {
    position: absolute; left: 0; right: 0; bottom: 0; height: 117px;
    background: var(--orange);
    display: flex; align-items: center; justify-content: center;
  }
  .signature-band__name { color: var(--white); font-weight: 700; font-size: 46px; line-height: 1; }
</style>
</head>
<body>
<main class="canvas">
  <section class="card card--front" aria-label="Card front">
    <div class="brand">
      <span class="brand__dot" aria-hidden="true"></span>
      <h1 class="brand__name">KEV.PRO</h1>
      <p class="brand__tagline">Darren Holcombe Fitness</p>
    </div>
    <div class="contact">
      <p class="contact__line"><span class="contact__label">Website:</span><span class="contact__value">www.kev-pro.example</span></p>
      <p class="contact__line"><span class="contact__label">Email:</span><span class="contact__value">dan@kev-pro.example</span></p>
    </div>
  </section>

  <section class="card card--back" aria-label="Card back">
    <span class="tab" aria-hidden="true"></span>
    <p class="quote">
      <span class="quote__line quote__line--lead">Take <span class="accent">Control</span></span>
      <span class="quote__line quote__line--small">Of your personal health</span>
      <span class="quote__line quote__line--small quote__line--indent">To unleash your</span>
      <span class="quote__line quote__line--close">Greatest <span class="accent">Potential</span></span>
    </p>
    <div class="signature-band">
      <span class="signature-band__name">KEV.PRO</span>
    </div>
  </section>
</main>
</body>
</html>
```